Business Card Design for Kidvale (Hires out childrens play areas)

Looking to have a business card designed for a company we just bought. The company rents out childrens play areas.

I have uploaded a couple of examples of the kind of business card style I like. Here are two more examples:

https://quorvastudio.nz/project/bright-romp-branding/
https://imgvaultcdn.com/design_img/8841052/302917/302917_5518203_8841052_b73e19a2_image.jpg

I think a white card will be best due to all the colours in the logo.

Size we require: 3.75" x 2.25" (horizontally orientated) with a 0.125" bleed

Uploaded is two versions of our logo.

Details for the card:
1. My name: Liam Verster
2. Title: Managing Director
3. Phone no: 021 563 417
4. Email: liam@kidvale.co.nz
5. URL: www.kidvale.co.nz
6. Address:
PO Box 318625
Fernlea, Auckland

Let me know if you need anything else.

Target Market(s)

Hospitals, doctors surgeries, bed shops, etc.

Contact Information for Business Card

Details for the card:
1. My name: Liam Verster
3. Phone no: 021 563 417
5. URL: www.kidvale.co.nz
6. Address:
PO Box 318625
Fernlea, Auckland

Requirements
Should not have
• Not too busy.

```html
<!DOCTYPE html>
<html lang="en">
<head>
<meta charset="UTF-8">
<title>Kidvale Business Card</title>
<link href="https://fonts.googleapis.com/css2?family=Nunito:wght@800&family=Questrial&display=swap" rel="stylesheet">
<style>
  :root {
    --page-bg: #efefef;
    --brand-purple: #7f2a8c;
    --card-white: #ffffff;
    --name-blue: #1e63b5;
    --name-red: #e8262d;
    --title-orange: #f7931e;
    --ink: #3a3a3a;
    --icon-purple: #7a2f8f;
    --mascot-top: #6c2c8e;
    --mascot-bottom: #e8168a;
  }
  * { margin: 0; padding: 0; box-sizing: border-box; }
  html, body {
    width: 1200px; height: 1200px; overflow: hidden;
    background: var(--page-bg);
    font-family: "Questrial", sans-serif;
  }
  .card {
    position: absolute; left: 198px; width: 804px; height: 460px; overflow: hidden;
  }
  .card--front { top: 124px; background: var(--brand-purple); }
  .card--back { top: 633px; background: var(--card-white); }

  .front-brand {
    position: absolute; left: 0; right: 0; top: 180px;
    text-align: center;
    font-family: "Nunito", sans-serif; font-weight: 800;
    font-size: 86px; line-height: 1; color: var(--card-white);
  }
  .front-url {
    position: absolute; left: 260px; top: 338px; width: 284px; height: 39px;
    border-radius: 20px; background: var(--card-white);
    color: var(--brand-purple);
    font-family: "Nunito", sans-serif; font-weight: 800; font-size: 21px;
    display: flex; align-items: center; justify-content: center;
  }

  .back-brand {
    position: absolute; left: 42px; top: 44px;
    font-family: "Nunito", sans-serif; font-weight: 800;
    font-size: 52px; line-height: 1; color: var(--brand-purple);
  }
  .person { position: absolute; left: 40px; top: 182px; }
  .person-name {
    font-family: "Nunito", sans-serif; font-weight: 800;
    font-size: 31px; line-height: 1;
  }
  .person-name .first { color: var(--name-blue); }
  .person-name .last { color: var(--name-red); }
  .person-title { color: var(--title-orange); font-size: 15px; margin-top: 2px; }

  .contact { position: absolute; left: 36px; top: 258px; list-style: none; }
  .contact li {
    display: flex; align-items: flex-start; gap: 12px;
    color: var(--ink); font-size: 22px; line-height: 26px; height: 39px;
  }
  .contact li.address { height: auto; }
  .contact svg { width: 24px; height: 24px; flex: none; margin-top: 2px; fill: var(--icon-purple); }
  .contact li.address svg { margin-top: 14px; }

  .mascot {
    position: absolute; left: 422px; top: 78px; width: 392px; height: 392px;
    border-radius: 50%;
    background: linear-gradient(180deg, var(--mascot-top), var(--mascot-bottom));
  }
</style>
</head>
<body>
  <section class="card card--front">
    <div class="front-brand">Kidvale</div>
    <div class="front-url">www.kidvale.co.nz</div>
  </section>

  <section class="card card--back">
    <div class="back-brand">Kidvale</div>

    <div class="person">
      <div class="person-name"><span class="first">Liam</span> <span class="last">Verster</span></div>
      <div class="person-title">Managing Director</div>
    </div>

    <ul class="contact">
      <li>
        <svg viewBox="0 0 24 24" aria-hidden="true"><path d="M6.6 10.8a15.1 15.1 0 0 0 6.6 6.6l2.2-2.2a1 1 0 0 1 1-.25 11.4 11.4 0 0 0 3.6.57 1 1 0 0 1 1 1V20a1 1 0 0 1-1 1A17 17 0 0 1 3 4a1 1 0 0 1 1-1h3.5a1 1 0 0 1 1 1c0 1.25.2 2.45.57 3.57a1 1 0 0 1-.25 1z"/></svg>
        <span>&nbsp;021 563 417</span>
      </li>
      <li>
        <svg viewBox="0 0 24 24" aria-hidden="true"><path d="M12 2a10 10 0 1 0 5 18.7l-1-1.7A8 8 0 1 1 20 12v1.2a1.8 1.8 0 0 1-3.6 0V12a4.4 4.4 0 1 0-1.3 3.1 3.8 3.8 0 0 0 6.9-1.9V12A10 10 0 0 0 12 2zm0 12.4a2.4 2.4 0 1 1 0-4.8 2.4 2.4 0 0 1 0 4.8z"/></svg>
        <span>liam@kidvale.co.nz</span>
      </li>
      <li>
        <svg viewBox="0 0 24 24" aria-hidden="true"><path d="M10.6 13.4a1 1 0 0 1 0-1.4l3.5-3.5a1 1 0 1 1 1.4 1.4L12 13.4a1 1 0 0 1-1.4 0zM8.5 20.5a4.2 4.2 0 0 1-3-7.2l2.4-2.4 1.4 1.4-2.4 2.4a2.2 2.2 0 1 0 3.1 3.1l2.4-2.4 1.4 1.4-2.4 2.4a4.2 4.2 0 0 1-2.9 1.3zm7.6-7.4-1.4-1.4 2.4-2.4a2.2 2.2 0 1 0-3.1-3.1l-2.4 2.4-1.4-1.4 2.4-2.4a4.2 4.2 0 1 1 5.9 5.9z"/></svg>
        <span>www.kidvale.co.nz</span>
      </li>
      <li class="address">
        <svg viewBox="0 0 24 24" aria-hidden="true"><path d="M12 3 2 12h3v8h5v-5h4v5h5v-8h3z"/></svg>
        <span>PO Box 318625<br>Fernlea, Auckland</span>
      </li>
    </ul>

    <div class="mascot" role="img" aria-label="Large brand mascot illustration in purple to pink tones"></div>
  </section>
</body>
</html>
```